Homemaking training schools needs a Business Card design

Designer, Hello!

No special requirements, good-looking enough.
--------------------------------------------------------------------------

Name: Marcus Dale
Chairman
Tel: 0574-31759426
Mobile: 13817450926
Email: brimwell@mailtor.com
Web: www.kvd2018.com
Add: No.382, QinglanJie, BaolinQu, Ningbo, Zhejiang

LOGO
Ningbo KVD Homemaking Training School

Target Market(s)

pregnant women, mothers, infants, the elderly and families, including cleaning, cooking, nursing training.

Industry/Entity Type

Business

Contact Information for Business Card

Name: Marcus Dale
Chairman
Tel: 0574-31759426
Mobile: 13817450926
Email: brimwell@mailtor.com
Web: www.kvd2018.com

LOGO

Font styles to use
Serif
Sans Serif
Decorative

Requirements
Nice to have
• Feels: clean, specifications, safety, comfort, warmth and happiness.

```html
<!DOCTYPE html>
<html lang="en">
<head>
<meta charset="utf-8">
<title>KaiVeDa Business Card</title>
<link href="https://fonts.googleapis.com/css2?family=Quicksand:wght@500;700&family=Montserrat:wght@500;600;700;800&display=swap" rel="stylesheet">
<style>
  :root {
    --brand-blue: #1274bf;
    --brand-pink: #e8088c;
    --ink-dark: #3a3a3a;
    --paper: #ffffff;
    --backdrop: #e9eaec;
  }
  * { margin: 0; padding: 0; box-sizing: border-box; }
  html, body { width: 1200px; height: 900px; overflow: hidden; }
  body {
    background: var(--backdrop);
    position: relative;
    font-family: "Montserrat", Arial, sans-serif;
  }
  .card {
    position: absolute;
    width: 700px;
    height: 400px;
    box-shadow: 0 6px 18px rgba(0,0,0,0.18);
  }
  .card--back {
    left: 110px; top: 40px;
    background: var(--brand-blue);
    display: flex; flex-direction: column; align-items: center; justify-content: center;
    color: var(--paper);
  }
  .card--front {
    left: 390px; top: 470px;
    background: var(--paper);
  }
  .brand {
    display: flex; align-items: center; gap: 14px;
    font-family: "Quicksand", Arial, sans-serif;
    font-weight: 700;
    line-height: 1;
  }
  .brand__dot { border-radius: 50%; background: var(--brand-pink); flex: none; }
  .card--back .brand { font-size: 78px; color: var(--paper); }
  .card--back .brand__dot { width: 30px; height: 30px; }
  .school-name {
    margin-top: 30px;
    font-size: 19px; font-weight: 700;
    color: var(--ink-dark);
  }
  .web-address {
    margin-top: 14px;
    font-size: 24px; font-weight: 700;
    color: var(--paper);
  }

  .feature-mark {
    position: absolute; left: 40px; top: 0;
    width: 290px; height: 400px;
    display: flex; flex-direction: column; align-items: center; justify-content: center;
    gap: 22px;
    font-family: "Quicksand", Arial, sans-serif;
    font-weight: 700;
    font-size: 58px;
    color: var(--brand-blue);
    line-height: 1;
  }
  .feature-mark__dot {
    width: 110px; height: 110px;
    border-radius: 50%;
    background: var(--brand-pink);
  }

  .card--front .identity {
    position: absolute; left: 360px; top: 52px;
    color: var(--brand-blue);
  }
  .card--front .brand { font-size: 50px; color: var(--brand-blue); }
  .card--front .brand__dot { width: 20px; height: 20px; }
  .person-name { margin-top: 26px; font-size: 28px; font-weight: 800; letter-spacing: 0.5px; line-height: 1.1; }
  .person-role { font-size: 14px; font-weight: 700; color: var(--ink-dark); letter-spacing: 1px; }
  .address { margin-top: 12px; font-size: 15px; font-weight: 600; line-height: 1.3; }
  .contacts { list-style: none; margin-top: 8px; font-size: 15px; font-weight: 600; }
  .contacts li { display: flex; align-items: center; gap: 10px; line-height: 1.45; }
  .contacts svg { width: 14px; height: 14px; flex: none; }
</style>
</head>
<body>
  <section class="card card--back">
    <div class="brand"><span class="brand__dot"></span>KaiVeDa</div>
    <p class="school-name">Ningbo KVD homemaking training school</p>
    <p class="web-address">www.kvd2018.com</p>
  </section>

  <section class="card card--front">
    <div class="feature-mark">
      <span class="feature-mark__dot"></span>
      <span class="feature-mark__name">KaiVeDa</span>
    </div>
    <div class="identity">
      <div class="brand"><span class="brand__dot"></span>KaiVeDa</div>
      <h1 class="person-name">MARCUS DALE</h1>
      <p class="person-role">CHAIRMAN</p>
      <p class="address">382, QinglanJie<br>BaolinQu, Ningbo, Zhejiang</p>
      <ul class="contacts">
        <li><svg viewBox="0 0 16 16"><path d="M4 1l3 3-2 2c1 2 3 4 5 5l2-2 3 3-2 3C7 15 1 9 1 3z" fill="#333"/></svg>0574-31759426</li>
        <li><svg viewBox="0 0 16 16"><rect x="4" y="1" width="8" height="14" rx="1.5" fill="none" stroke="#333" stroke-width="1.6"/><circle cx="8" cy="12.5" r="0.9" fill="#333"/></svg>13817450926</li>
        <li><svg viewBox="0 0 16 16"><rect x="1" y="3" width="14" height="10" fill="none" stroke="#333" stroke-width="1.6"/><path d="M1 3l7 6 7-6" fill="none" stroke="#333" stroke-width="1.6"/></svg>brimwell@mailtor.com</li>
        <li><svg viewBox="0 0 16 16"><circle cx="8" cy="8" r="6.5" fill="none" stroke="#333" stroke-width="1.4"/><path d="M1.5 8h13M8 1.5c-3 3.5-3 9.5 0 13M8 1.5c3 3.5 3 9.5 0 13" fill="none" stroke="#333" stroke-width="1.2"/></svg>www.kvd2018.com</li>
      </ul>
    </div>
  </section>
</body>
</html>
```